Corvana Power Holdings Website

We have color scheme, logo and content, but need a design options in PDF format for the website. The PDF should guide us in how to use the color scheme and fonts in the site design (what background colors to use where, what link and hover colors to you, when to use which fonts...)

Corvana Power Holdings wants a conservative and straightforward website design that is in line with the banking industry. At the same time, Corvana wants the design to be innovative and cutting-edge in line with the renewable energy industry. Overall, the site design must be present the company as professional, serious, knowledgeable, experienced, reliable, and successful as well as a global good citizen.
Updates

We are closing this project. Thank you all for your beautiful work. Our designer was sick, but informed us today that she is better and able to resume her work. So we are closing this project and restarting work with her. Wish you all health and success.

Target Market(s)

investors, partners, developers, investment community, private equity community

Industry/Entity Type

Investment

Number of Pages Required

2 page

Requirements
Must have
• The color scheme is attached.
The logo is attached.
Fonts are Questrial and Cormorant (as used in logo).
The site must use these colors and fonts and logo design.

The 2 pages we need designed are the homepage and the portfolio page.
Homepage - The portfolio map on the homepage will be an image like with hotspots that link to portfolio items. This map image might go well with logo:
https://www.pixdrovo.com/abstract-polygon-world-map-vector-illustration-geometric-structure-in-blue-color-for-presentation-booklet-website-and-other-design-projects-pol-image550392817.html
But we would need to zoom in on Israel and EU, and leave out US / Asia-Pacific.
The way the map will work technically (using hotspots) should be something like:
https://tarvimpower.co.il/geographic-spread/.
Portfolio Page - The portfolio map there will be a Google Map/
Nice to have
• The content for the site is attached as a Word Doc, and much of it is in place at http://corvanafund.com.node4821.hostmarvo.de/. The design must fit this content, but we are open to some layout changes.
Design Requests:
• nav bar – light animation like https://pelludovet.com/ and https://www.qz-relocationlaw.com/
• innovative, unique design with welcoming, appealing, modern feel
• engaging content display by using parallax and subtle movement
• clean, intuitive, easy to navigation layout

```html
<!DOCTYPE html>
<html lang="en">
<head>
<meta charset="utf-8">
<title>Corvana Power Holdings</title>
<link rel="stylesheet" href="https://fonts.googleapis.com/css2?family=Cormorant+Garamond:wght@500;600;700&family=Questrial&display=swap">
<style>
:root{
  --green:#a6d23a;
  --green-dark:#2f6b2a;
  --blue:#1a8fc4;
  --teal:#0f86b0;
  --sky:#58b8e0;
  --orange:#f4a35c;
  --ink:#333;
  --muted:#666;
  --footer:#2a2a2a;
  --white:#fff;
  --serif:"Cormorant Garamond", Georgia, serif;
  --sans:"Questrial", Arial, sans-serif;
}
*{box-sizing:border-box;margin:0;padding:0}
html,body{width:1200px;height:2884px;overflow:hidden}
body{position:relative;background:var(--white);font-family:var(--sans);color:var(--ink)}

.site-header{position:absolute;top:0;left:0;width:1200px;height:76px;z-index:3;display:flex;align-items:center;justify-content:space-between;padding:0 110px 0 110px;background:rgba(255,255,255,.92)}
.brand{display:flex;align-items:center;gap:12px;font-family:var(--serif);font-weight:700;font-size:30px;color:var(--green-dark);letter-spacing:1px}
.brand-dot{width:26px;height:26px;border-radius:50%;background:var(--green)}
.main-nav{display:flex;gap:44px;font-size:15px;letter-spacing:1px;color:var(--ink)}

.hero{position:absolute;top:0;left:0;width:1200px;height:620px;background:linear-gradient(180deg,#c8d3dc 0%,#aebcc6 35%,#8a9a86 70%,#6f7f63 100%)}
.hero-title{position:absolute;top:218px;left:248px;width:744px;height:124px;background:rgba(255,255,255,.72);text-align:center;padding-top:10px}
.hero-title h1{font-family:var(--serif);font-weight:600;font-size:46px;letter-spacing:2px;color:var(--green-dark)}
.hero-title p{font-size:19px;line-height:26px;color:var(--ink)}

.stats{position:absolute;top:452px;left:232px;display:flex;gap:6px}
.stat{width:180px;height:180px;border-radius:50%;display:flex;flex-direction:column;align-items:center;justify-content:center;text-align:center;font-family:var(--serif);font-weight:600;color:#1d2b3a;font-size:22px;line-height:24px;border:4px solid rgba(255,255,255,.85)}
.stat strong{font-size:28px;margin-bottom:2px}
.stat--green{background:var(--green)}
.stat--sky{background:var(--sky)}
.stat--orange{background:var(--orange)}
.stat--teal{background:var(--teal);color:var(--white)}

.pillars{position:absolute;top:772px;left:0;width:1200px;height:380px;display:flex}
.pillar{width:600px;height:380px;padding:96px 58px 0 58px;color:var(--ink)}
.pillar--green{background:linear-gradient(135deg,#b9dc4e,#9ccb35)}
.pillar--blue{background:linear-gradient(135deg,#2fa0cf,#1680b5);color:var(--white)}
.pillar h2{font-family:var(--serif);font-weight:600;font-size:30px;letter-spacing:1px;line-height:34px;margin-bottom:18px}
.pillar p{font-size:17px;line-height:25px;max-width:440px;margin-bottom:14px}
.link{font-family:var(--serif);font-weight:700;font-size:18px;letter-spacing:1px;text-decoration:underline}

.strategy{position:absolute;top:1300px;left:110px;width:980px;height:320px}
.strategy-text{position:absolute;left:0;top:40px;width:520px}
.strategy h2{font-family:var(--serif);font-weight:600;font-size:44px;line-height:46px;letter-spacing:1px;color:#222;margin-bottom:30px}
.strategy p{font-size:15px;line-height:24px;color:var(--muted);text-align:justify;margin-bottom:30px}
.strategy .link{color:#222}
.strategy-photo{position:absolute;left:546px;top:0;width:312px;height:312px;border-radius:50%;border:6px solid var(--green);background:linear-gradient(180deg,#6ea3c8 0%,#a9c7d9 55%,#9fae82 80%,#7f8c60 100%)}

.portfolio-intro{position:absolute;top:1756px;left:200px;width:800px;text-align:center;font-size:17px;line-height:28px;color:var(--ink)}
.portfolio-map{position:absolute;top:1836px;left:100px;width:1000px;height:700px;background:radial-gradient(ellipse at 25% 45%,#2b7fc2 0%,#37a6d8 25%,transparent 45%),radial-gradient(ellipse at 60% 35%,#c9dd3e 0%,#f1c532 30%,transparent 55%),radial-gradient(ellipse at 80% 70%,#f4a030 0%,#ef7c28 30%,transparent 50%),#fff}

.site-footer{position:absolute;top:2608px;left:0;width:1200px;height:276px;background:var(--footer);color:#cfcfcf}
.footer-cols{position:absolute;top:48px;left:0;width:1200px;display:flex;justify-content:space-around;padding:0 120px}
.footer-col{width:300px;text-align:center;font-size:14px;line-height:22px}
.footer-col svg{display:block;margin:0 auto 12px}
.footer-col h3{font-size:14px;font-weight:400;letter-spacing:1px;color:var(--white);margin-bottom:8px}
.footer-copy{position:absolute;left:0;top:226px;width:1200px;text-align:center;font-size:13px;color:#aaa}
.footer-lang{position:absolute;right:60px;top:226px;font-size:13px;color:#aaa}
</style>
</head>
<body>

<div class="hero" role="img" aria-label="Aerial photo of a solar and power plant field under a pale sky"></div>

<header class="site-header">
  <div class="brand"><span class="brand-dot"></span>Corvana Power Holdings</div>
  <nav class="main-nav"><span>HOME</span><span>ABOUT</span><span>STRATEGY</span><span>PORTFOLIO</span><span>CONTACT</span></nav>
</header>

<section class="hero-title">
  <h1>ILLUMINATING THE FUTURE</h1>
  <p>Investing in clean energy to generate sustainable returns<br>for our investors and planet</p>
</section>

<div class="stats">
  <div class="stat stat--green"><strong>10</strong>Years of<br>Operation</div>
  <div class="stat stat--sky"><strong>6</strong>Countries of<br>Investment</div>
  <div class="stat stat--orange"><strong>600</strong>Assets under<br>Management</div>
  <div class="stat stat--teal"><strong>$1,000,000,000</strong>Assets under<br>Management</div>
</div>

<section class="pillars">
  <div class="pillar pillar--green" role="img" aria-label="Green-tinted photo of a solar park">
    <h2>EXPERTISE, RESOURCEFULNESS,<br>INTEGRITY</h2>
    <p>Funding clean energy projects that maximize value to our investors and contribute to a more sustainable world</p>
    <span class="link">ABOUT US</span>
  </div>
  <div class="pillar pillar--blue" role="img" aria-label="Blue-tinted photo of wind turbines">
    <h2>HANDS-ON INVESTMENT<br>MANAGEMENT</h2>
    <p>Utilizing our multi-disciplinary knowledge, sector expertise, extensive experience and collaborative spirit</p>
    <span class="link">OUR TEAM</span>
  </div>
</section>

<section class="strategy">
  <div class="strategy-text">
    <h2>PROVEN INVESTMENT<br>STRATEGY</h2>
    <p>Achieving consistently high annualized returns and capital gains by leveraging our energy sector experience, broad geographic footprint, dedicated local networks, value creation and implementation of platform structures.</p>
    <span class="link">OUR APPROACH</span>
  </div>
  <div class="strategy-photo" role="img" aria-label="Photo of a single wind turbine against the sky"></div>
</section>

<p class="portfolio-intro">Corvana' energy funds provide a diversified portfolio of assets- in operation and under construction, in multiple markets -that drive high investment returns and a balanced risk profile.</p>

<div class="portfolio-map" role="img" aria-label="Colourful polygon world map with portfolio location markers in Europe and Israel"></div>

<footer class="site-footer">
  <div class="footer-cols">
    <div class="footer-col">
      <svg width="30" height="30" viewBox="0 0 30 30"><circle cx="15" cy="15" r="14" fill="none" stroke="#a6d23a" stroke-width="1.5"/><path d="M10 8l3 0 1.5 4-2 1.5a9 9 0 0 0 4 4l1.5-2 4 1.5v3a2 2 0 0 1-2 2A13 13 0 0 1 8 10a2 2 0 0 1 2-2z" fill="#a6d23a"/></svg>
      <h3>PHONE</h3>
      Israel: +972-3-555-0142<br>Europe: +44 (0)20 7946 0318
    </div>
    <div class="footer-col">
      <svg width="30" height="30" viewBox="0 0 30 30"><circle cx="15" cy="15" r="14" fill="none" stroke="#a6d23a" stroke-width="1.5"/><path d="M15 7a6 6 0 0 1 6 6c0 4.5-6 10-6 10s-6-5.5-6-10a6 6 0 0 1 6-6z" fill="#a6d23a"/><circle cx="15" cy="13" r="2.2" fill="#2a2a2a"/></svg>
      <h3>ADDRESS</h3>
      Corvana Power Holdings, Lumen Tower,<br>12 Orchard Way, Ramat Tavor 47100 Israel
    </div>
    <div class="footer-col">
      <svg width="30" height="30" viewBox="0 0 30 30"><circle cx="15" cy="15" r="14" fill="none" stroke="#a6d23a" stroke-width="1.5"/><rect x="8" y="10" width="14" height="10" fill="none" stroke="#a6d23a" stroke-width="1.5"/><path d="M8 10l7 6 7-6" fill="none" stroke="#a6d23a" stroke-width="1.5"/></svg>
      <h3>EMAIL</h3>
      info@corvanafund.com
    </div>
  </div>
  <p class="footer-copy">© 2020 All Rights Reserved</p>
  <span class="footer-lang">עב</span>
</footer>

</body>
</html>
```